We need a brochure designed for a presentation to a new client based around the use of Horizontal Directional Drilling and the installation of culverts with its use. Not all photos are required to be used.
The process used to install culverts is as follows:1)Survey the site and grade changes2)Set up drill to required pitch3)Drill pilot bore4)Pre-ream to required diameter5)Assemble culverts and install pulling adapter6)Pull culvert back behind reamer7)Install requested aggregate material around culvert ends. Horizontal Directional Drilling is on average 30% less in cost compared to traditional open excavation methods and can generally be completed 40% faster. HDD can be used to install a large amount of different products. For example you can install corrugated(culverts), steel pipe, HDPE pipe, PVC pipe, and many more. The following industries have benefitted from the use of trenchless technology over the years: Oil & Gas, Power & Telecommunications, Highway & road Construction, Water and sewer. HDD provides a safer and more cost effective alternative to open cut methods by allowing traffic to flow without disruption and limit the time workers and crew members have to spend on road ways and trenches providing a safer work environment.

Target Market(s)

new clients and local highway improvement governments

Colors

Designer to choose colors to be used in the design.

Requirements
Must have
• Provide some pictures, description of how to do the installation, cost advantages with a graph or pie chart, and the safety factors
Nice to have
• Types of product that can be installed and industries that use the technology
• Or company colours are black, grey, and orange
Should not have
• no false information or misleading info

```html
<!DOCTYPE html>
<html lang="en">
<head>
<meta charset="utf-8">
<title>Horizontal Directional Drilling Brochure</title>
<link href="https://fonts.googleapis.com/css2?family=Arimo:ital,wght@0,400;0,700;1,400&family=Yanone+Kaffeesatz:wght@300;700&display=swap" rel="stylesheet">
<style>
  :root{
    --orange:#f15a24;
    --grey:#8c8c8c;
    --dark:#1e1e1e;
    --white:#ffffff;
    --stage:#e4e4e4;
  }
  html,body{margin:0;padding:0;overflow:hidden;}
  body{width:1200px;height:1198px;background:var(--stage);position:relative;font-family:"Arimo",Arial,sans-serif;}
  .page{position:absolute;top:243px;width:520px;height:712px;background:var(--white);overflow:hidden;box-shadow:0 6px 18px rgba(0,0,0,.25);}
  .page--back{left:60px;}
  .page--cover{left:620px;}
  .page svg.shapes{position:absolute;inset:0;width:520px;height:712px;}
  /* back page */
  .process{position:absolute;left:22px;top:16px;width:470px;font-size:11.3px;line-height:12.6px;color:var(--dark);}
  .process h2{margin:0 0 1px;font-size:11.5px;font-weight:700;}
  .process ul{list-style:none;margin:0;padding:0 0 0 36px;}
  .process li{position:relative;padding-left:28px;}
  .process li::before{content:"";position:absolute;left:0;top:2px;width:9px;height:9px;border-radius:50%;background:var(--orange);}
  .process p{margin:0 0 4px;}
  .industries{margin:2px 0 4px 128px;color:var(--orange);font-style:italic;line-height:11.6px;}
  .safety{margin:0 0 0 150px;width:320px;text-align:center;}
  .cost-chart{position:absolute;left:24px;top:588px;width:220px;height:86px;}
  .cost-chart text{font-family:"Arimo",Arial,sans-serif;fill:var(--white);font-size:9.5px;}
  .cost-chart .chart-title{font-weight:700;font-size:10.5px;}
  .back-brand{position:absolute;left:230px;top:548px;width:270px;text-align:center;color:var(--white);}
  .brand-dot{display:inline-block;width:40px;height:40px;border-radius:50%;background:var(--white);}
  .brand-name{font-family:"Arimo",Arial,sans-serif;font-weight:700;font-size:16px;letter-spacing:.5px;line-height:18px;margin-top:4px;white-space:nowrap;}
  .contact{position:absolute;right:24px;top:636px;text-align:right;color:var(--dark);font-size:11px;line-height:14px;}
  .website{position:absolute;left:0;width:100%;top:682px;text-align:center;color:var(--white);font-weight:700;font-size:14px;letter-spacing:1px;}
  /* cover */
  .cover-title{position:absolute;left:30px;top:30px;margin:0;font-family:"Yanone Kaffeesatz",sans-serif;font-weight:700;font-size:52px;line-height:42px;color:var(--white);}
  .cover-brand{position:absolute;left:340px;top:26px;width:170px;text-align:center;}
  .cover-brand .brand-dot{background:none;border:4px solid var(--orange);width:46px;height:46px;}
  .cover-brand .brand-name{color:var(--orange);font-size:19px;white-space:normal;}
  .cover-tagline{position:absolute;left:30px;top:588px;margin:0;font-family:"Yanone Kaffeesatz",sans-serif;font-size:42px;line-height:36px;color:var(--white);}
  .cover-tagline .light{font-weight:300;}
  .cover-tagline .bold{font-weight:700;}
</style>
</head>
<body>

<section class="page page--back">
  <svg class="shapes" viewBox="0 0 520 712">
    <defs>
      <linearGradient id="toolsPhoto" x1="0" y1="0" x2="1" y2="1">
        <stop offset="0" stop-color="#c9c9c9"/>
        <stop offset="0.5" stop-color="#9a9a9a"/>
        <stop offset="1" stop-color="#7a7a7a"/>
      </linearGradient>
    </defs>
    <g role="img" aria-label="Photo of a corrugated culvert section and a drilling reamer lying on a shop floor">
      <rect x="0" y="240" width="520" height="340" fill="url(#toolsPhoto)"/>
    </g>
    <polygon points="0,0 520,0 520,269 320,384 0,240" fill="var(--white)"/>
    <polygon points="333,0 520,0 520,122" fill="var(--orange)"/>
    <polygon points="0,566 338,493 520,521 520,712 0,712" fill="var(--orange)"/>
  </svg>

  <div class="process">
    <h2>The process used to install culverts is as follows:</h2>
    <ul>
      <li>Determine amount of grade change</li>
      <li>Set up drill to required pitch</li>
      <li>Drill across desired area with pilot hole</li>
      <li>Install reamer and do multiple passes until hole is clean<br>and at desired diameter</li>
      <li>Assemble culverts and install pulling adapter</li>
      <li>Pull culvert back behind reamer</li>
      <li>Install requested aggregate material around culvert ends Horizontal</li>
    </ul>
    <p>Directional Drilling is on average 30% less in cost compared to traditional open cutting methods and can provide competition times at almost 40% faster rate.</p>
    <p>HDD can be used to install a large amount of different products with all kinds of uses and sizes. For example you can install corrugated(culverts), steel culverts, HDPE pipe, PVC pipe, and insulated water lines to name a few. The following industries have benefitted from the use of trenches technology over the years:</p>
    <div class="industries">Oil &amp; Gas,<br>Telecom infrastructure,<br>Power infrastructure,<br>Highway &amp; road Construction,<br>Water and sewer and irrigation situations.</div>
    <p class="safety">HDD provides a safer and more cost effective alternative to open cut methods by allowing traffic to flow without disruption and limit the time workers and crew members have to spend on road ways and areas with limited access.</p>
  </div>

  <svg class="cost-chart" viewBox="0 0 220 86" role="img" aria-label="Bar chart: HDD costs about 30% less and takes about 40% less time than open cut">
    <text class="chart-title" x="0" y="10">HDD vs open cut (average)</text>
    <text x="0" y="27">Cost</text>
    <rect x="38" y="19" width="140" height="9" fill="var(--white)" opacity=".55"/>
    <text x="182" y="27">100%</text>
    <rect x="38" y="31" width="98" height="9" fill="var(--white)"/>
    <text x="140" y="39">70%</text>
    <text x="0" y="61">Time</text>
    <rect x="38" y="53" width="140" height="9" fill="var(--white)" opacity=".55"/>
    <text x="182" y="61">100%</text>
    <rect x="38" y="65" width="84" height="9" fill="var(--white)"/>
    <text x="126" y="73">60%</text>
    <rect x="0" y="79" width="7" height="6" fill="var(--white)" opacity=".55"/>
    <text x="10" y="85" font-size="8">Open cut</text>
    <rect x="58" y="79" width="7" height="6" fill="var(--white)"/>
    <text x="68" y="85" font-size="8">HDD</text>
  </svg>

  <div class="back-brand">
    <span class="brand-dot"></span>
    <div class="brand-name">RIDGELINE BORING INC</div>
  </div>
  <div class="contact">18 Tamarack Rd, Northvale, YT Y0B 1C4<br>867-555-0142</div>
  <div class="website">www.ridgelineboring.com</div>
</section>

<section class="page page--cover">
  <svg class="shapes" viewBox="0 0 520 712">
    <defs>
      <linearGradient id="crewPhoto" x1="0" y1="0" x2="1" y2="1">
        <stop offset="0" stop-color="#6b5e50"/>
        <stop offset="0.5" stop-color="#3a3835"/>
        <stop offset="1" stop-color="#a9aeb3"/>
      </linearGradient>
    </defs>
    <g role="img" aria-label="Photo of a crew member in hi-vis winter gear fitting a pulling adapter to a corrugated culvert in a muddy trench">
      <polygon points="0,250 323,143 520,256 520,712 0,712" fill="url(#crewPhoto)"/>
    </g>
    <polygon points="0,0 198,0 323,143 0,250" fill="var(--orange)"/>
    <polygon points="0,435 343,712 0,712" fill="var(--grey)"/>
    <polygon points="436,712 520,614 520,712" fill="var(--orange)"/>
  </svg>

  <h1 class="cover-title">Horizontal<br>Directional<br>Drilling</h1>
  <div class="cover-brand">
    <span class="brand-dot"></span>
    <div class="brand-name">RIDGELINE<br>BORING INC</div>
  </div>
  <p class="cover-tagline"><span class="bold">Installation</span><br><span class="light">of</span> <span class="bold">culverts</span><br><span class="light">with its</span> <span class="bold">use</span></p>
</section>

</body>
</html>
```